Harrowby Wine Label - Design a front and smaller back label for an exclusive red wine

Harrowby Wines produces a very high quality, high priced wine from an old and prestigous vineyard in one of Australia's oldest, but smallest wine growing regions. The grapevines are old (like old men with gnarled arms and trunks) and they produce fewer grapes than younger vines but the grape quality (and thus wine quality) is magnificent and highly sought after as it produces wine of exceptional quality.
The vineyard was purchased by the Harrowby family in February 2010 from a multinational wine company who made wonderful, trophy winning wines for 10 years before the vineyard went into a decline.
The challenge is to produce 2 labels - a simple main front label that focuses on the Harrowby brand and a smaller, information rich, back label that relates the history of the vineyard.
The labels should have a white or charcoal grey background and impart tradition, quality, exclusivity and a little self indulgence which is why we want the family crest incorporated - the choice of font will help.
It might also impart a sense of fun so that it appeals to the 25-35 year old age bracket.
The label should be kept clean and simple not loud and busy. Preferred colours are black, grey and white. Red is fine if used sparingly

Here are the details:_

Front Label (115 long x 65-90mm wide)

Harrowby
Lanternwatch Reserve
2011
Mudgee
Wine of Australia 750ml

Back Label (dimensions to suit text and front label design; font size small; text in black so that it is readable in less than optimal light (eg candlelight at a restaurant table).

Harrowby
Lanternwatch Reserve 2011

This is the first release of The Lanternwatch’s Reserve – just 100 dozen bottles were made. The wine was made from Shiraz and 10% Cabernet Sauvignon grapes sourced from an iconic Mudgee vineyard that was established 1966 by Peter Vallis. In 1994, the vineyard known as ”Silver Hollow”, became the source of a decade of formidable, trophy winning wines under Tindalberg’s and later Quellwood’s ownership. The 20ha vineyard was purchased by Corin & Margaret Harrowby in 2010. The Silver Hollow name was retained by Quellwoods; no wine has been released under this label since the 2006 vintage.

The shaky old Shiraz vines are slowly being restored to full health using careful cane pruning techniques that stimulates fresh, new tissue growth, more even bunch sizes and better grape quality and consistency. The Shiraz grapes used in this wine were hand-picked from two rows of the first crop from the 46 year old, cane pruned vines. The 2011 Reserve is the first step to re-establish the traditions of a famous vineyard and one of Australia’s most sought after export wines.

“Deep and intense purple hues with aromas of ripe blackberry fruits, spice and eucalypt with rich chocolate complemented by subtle oak overtones. A rich and full bodied wine exhibiting a soft yet generous palate with plum, forest fruits and mint chocolate notes. A fine grained tannin structure displaying integrated oak characters adds to the complexity of the wine. This wine was aged for 18 months in a blend of new French oak hogsheads and one year old American hogsheads, crafting a blend with great structure and length of flavour which will develop into a Mudgee classic” – Lewis Farrant, Winemaker

13.5% Alc/Vol.
Contains approx 8.0 std drinks
Preservative (220) added

Harrowby Wines
Tallowbend Rd, Mudgee 2850
www.harrowbywines.example.au

Reason: My apologies to the designers who have kindly submitted some wonderful designs. I am trying to achieve a conscentious between shareholders. This is difficult as they are in different parts of the world and I have learned through this experience that opinions on wine labels are quite diverse!!! The feedback I have received so far indicates the following (1) A light or white background is preferred (2) The crest should not be a dominant part of the label (3) The label needs to be clean, fresh and uncomplicated (4) If red is used it should be in minor detail only (5) "Harrowby" should be distinctive. The font is difficult for us! (6) We are considering "The Lanternwatch" RESERVE instead of "Lanternwatch's" RESERVE (7) The text on the back label is too long; I will edit and re-upload Many thanks for your help and patience Kind regards Corin

Good Morning All,
I have edited the back label text to reduce the size of the label. A Word file with the changes has just been uploaded.
Cheers
Corin

Dear Designers,
Thank you all so very much for the wonderful selection of designs you have submitted my family have all been overwhelmed by the quality and skill level exhibited and we all appreciate you your efforts
Kindest regards
Corin

Target Market(s)

25-35 year old men and women of Australia, China, US & UK

Industry/Entity Type

Restaurant

Requirements
Must have
• Crest
Should not have
• Animals on the label

```html
<!DOCTYPE html>
<html lang="en">
<head>
<meta charset="utf-8">
<title>Harrowby — The Lanternwatch Reserve 2011</title>
<link rel="stylesheet" href="https://fonts.googleapis.com/css2?family=Montserrat:wght@400;500;600&family=Pinyon+Script&display=swap">
<style>
  :root {
    --label-cream: #fcfcec;
    --ink: #151515;
    --reserve-red: #e8201c;
    --crest-grey: #9a9a96;
    --crest-light: #e4e4dc;
  }
  html, body {
    margin: 0;
    padding: 0;
    overflow: hidden;
    background: var(--label-cream);
  }
  .label {
    position: relative;
    width: 745px;
    height: 1200px;
    background: var(--label-cream);
    color: var(--ink);
    font-family: "Montserrat", Arial, sans-serif;
    overflow: hidden;
  }
  .brand-name {
    position: absolute;
    top: 30px;
    left: 0;
    width: 745px;
    height: 100px;
    margin: 0;
  }
  .brand-name text {
    font-family: "Montserrat", Arial, sans-serif;
    font-size: 64px;
    font-weight: 500;
    letter-spacing: 4px;
    fill: var(--ink);
  }
  .family-crest {
    position: absolute;
    top: 124px;
    left: 232px;
    width: 274px;
    height: 299px;
  }
  .wine-title {
    position: absolute;
    top: 540px;
    left: 0;
    width: 100%;
    margin: 0;
    text-align: center;
    font-weight: 500;
  }
  .wine-title .article {
    display: block;
    font-family: "Pinyon Script", "Times New Roman", cursive;
    font-size: 112px;
    line-height: 112px;
    font-weight: 400;
    margin-left: -16px;
  }
  .wine-title .name {
    display: block;
    font-family: "Montserrat", Arial, sans-serif;
    font-size: 72px;
    line-height: 84px;
    font-weight: 500;
    letter-spacing: -0.5px;
  }
  .vintage-row {
    position: absolute;
    top: 762px;
    left: 0;
    width: 100%;
    height: 92px;
  }
  .vintage-row .year,
  .vintage-row .region {
    position: absolute;
    font-size: 32px;
    font-weight: 600;
    line-height: 1;
  }
  .vintage-row .year { left: 208px; top: 30px; letter-spacing: 1.5px; }
  .vintage-row .region { left: 453px; top: 26px; letter-spacing: 0.5px; }
  .keys-emblem {
    position: absolute;
    left: 320px;
    top: 0;
    width: 103px;
    height: 92px;
  }
  .reserve-mark {
    position: absolute;
    top: 888px;
    left: 0;
    width: 100%;
    margin: 0;
    text-align: center;
    font-size: 54px;
    font-weight: 600;
    letter-spacing: 1px;
    line-height: 1;
    color: var(--reserve-red);
  }
  .origin {
    position: absolute;
    top: 1117px;
    left: 0;
    width: 100%;
    margin: 0;
    text-align: center;
    font-size: 31px;
    font-weight: 400;
    letter-spacing: 1.5px;
    line-height: 1;
  }
</style>
</head>
<body>
  <main class="label">
    <svg class="brand-name" viewBox="0 0 745 100" role="heading" aria-level="1" aria-label="Harrowby">
      <defs>
        <path id="brand-arc" d="M 120 86 Q 372 40 625 86"/>
      </defs>
      <text text-anchor="middle"><textPath href="#brand-arc" startOffset="50%">HARROWBY</textPath></text>
    </svg>

    <svg class="family-crest" viewBox="0 0 274 299" role="img" aria-label="Harrowby family crest: motto ribbon, crown and shield with gates and battlements">
      <defs>
        <linearGradient id="crest-tone" x1="0" y1="0" x2="0" y2="1">
          <stop offset="0" stop-color="var(--crest-grey)"/>
          <stop offset="0.72" stop-color="var(--crest-grey)"/>
          <stop offset="0.8" stop-color="var(--crest-light)"/>
          <stop offset="1" stop-color="var(--crest-light)"/>
        </linearGradient>
      </defs>
      <path d="M0 60 Q137 -10 274 60 L274 100 L242 100 L242 240 Q242 280 137 299 Q32 280 32 240 L32 100 L0 100 Z" fill="url(#crest-tone)"/>
    </svg>

    <h2 class="wine-title">
      <span class="article">The</span>
      <span class="name">LANTERNWATCH</span>
    </h2>

    <div class="vintage-row">
      <span class="year">2011</span>
      <svg class="keys-emblem" viewBox="0 0 103 92" role="img" aria-label="Crossed keys emblem">
        <rect x="0" y="0" width="103" height="92" fill="var(--ink)"/>
      </svg>
      <span class="region">MUDGEE</span>
    </div>

    <p class="reserve-mark">RESERVE</p>

    <p class="origin">WINE OF AUSTRALIA</p>
  </main>
</body>
</html>
```